(The Tide Lady) Cleaning swimming pool's & Spa's weekly for a monthly Rate

Name of company is (KRT Pool & Spa Cleaning) Lic.# 318604 __ KRT are initials for Kathy Rose Tellez, a female owner, nick name for her and company is (The Tide Lady) we would like to see Company and Nick name plus Lic. # on post card along with contact # 951-478-2051 call or Text and e-mail address(k_kwaterfresh@mailvale.com) No business Address posted being its our home address, also post an incentive to use our service as follows (50% off First Month of Maintenance, Very Reasonable Rate's !! ) incentive written in the middle of a picture of a Gorgeous swimming pool and to one side of picture is the silhouette profile of a woman with or without holding a pole with a cleaning net at end of pole, color of card maybe different shades of blue or just all blue. what we provide is a weekly cleaning maintenance service on in ground swimming pool's & Spa's, Thank you, Kathy

Target Market(s)

Home Owners with in ground swimming pools

Industry/Entity Type

It Company

Font styles to use
Serif
Decorative
Script

Requirements
Must have
• Silhouette outline profile design or picture of a woman next to a elegant swimming pool, colors of outline woman are to be contrast color like a pink or light grey against a blue background postcard
Nice to have
• nick name(The Tide Lady) and company name (KRT Pool & Spa Cleaning) on postcard, A small logo of a bar and shield stamp on one corner of card, KRT should read on bar, upper half of shield CLEAN should read and bottom half P00LS should read. uploaded files show bar and shield and possible picture of woman
Should not have
• None

```html
<!DOCTYPE html>
<html lang="en">
<head>
<meta charset="utf-8">
<title>KRT Pool &amp; Spa Cleaning — Postcard</title>
<link rel="stylesheet" href="https://fonts.googleapis.com/css2?family=Damion&family=Oswald:wght@500;600&family=Roboto+Condensed:wght@700&family=Open+Sans:wght@600;700&display=swap">
<style>
  :root {
    --navy: #1a4f86;
    --deep: #0e5b8f;
    --mid: #2a86c3;
    --sky: #2a90cf;
    --cyan: #5cc6ef;
    --pale: #e4f2f8;
    --ice: #eaf4fb;
    --white: #ffffff;
    --stage: #dfe3e6;
    --rule: #b9bec4;
  }
  * { margin: 0; padding: 0; box-sizing: border-box; }
  html, body { width: 822px; height: 1200px; overflow: hidden; }
  body { background: var(--stage); font-family: "Open Sans", sans-serif; position: relative; }
  .card { position: absolute; width: 672px; height: 520px; overflow: hidden; box-shadow: 0 6px 18px rgba(0,0,0,.25); }
  .card--front { left: 32px; top: 40px; }
  .card--back { left: 104px; top: 630px; background: linear-gradient(180deg, var(--white), var(--ice)); }
  .layer { position: absolute; left: 0; top: 0; }
  .abs { position: absolute; white-space: nowrap; }
  .pool-photo { position: absolute; left: 0; top: 50px; width: 672px; height: 410px;
    background: linear-gradient(180deg, #2f3a2e 0%, #4d5a48 30%, #8a8f80 48%, #6fb7cf 62%, #a9dbe8 80%, #b8b4a8 100%); }
  .company { font-family: "Oswald", sans-serif; font-weight: 600; color: var(--navy); text-transform: uppercase; }
  .nickname { font-family: "Damion", cursive; color: var(--navy); }
  .brand { font-family: "Oswald", sans-serif; font-weight: 600; color: var(--navy); display: flex; align-items: center; }
  .brand-square { background: var(--mid); flex: none; }
  .license { font-family: "Open Sans", sans-serif; font-weight: 700; }
  .offer-big { font-family: "Roboto Condensed", sans-serif; font-weight: 700; color: var(--white); text-shadow: 2px 2px 3px rgba(0,40,80,.8); line-height: 1; }
  .offer-line { font-family: "Roboto Condensed", sans-serif; font-weight: 700; color: var(--white); font-size: 20px; text-shadow: 1px 1px 2px rgba(0,40,80,.9); }
  .insured { font-size: 10px; color: var(--navy); letter-spacing: 1px; }
  .service { font-weight: 600; font-size: 13px; color: var(--white); line-height: 20px; text-transform: uppercase; letter-spacing: .5px; white-space: normal; width: 280px; }
  .prompt { font-weight: 600; }
  .phone { font-weight: 700; }
  .portrait { position: absolute; left: 42px; top: 320px; width: 148px; height: 146px; border-radius: 50%;
    border: 5px solid #4bb0e6; background: linear-gradient(180deg, #8fb7a8, #6f9a6a); }
  .splash { position: absolute; left: 192px; top: 320px; width: 128px; height: 140px; border-radius: 14px;
    background: linear-gradient(160deg, #bfe4f7, #5ab6e6); opacity: .75; }
  .stamp-box { position: absolute; left: 546px; top: 23px; width: 96px; height: 80px; border: 2px solid var(--rule); }
  .address-line { position: absolute; left: 403px; width: 243px; height: 0; border-top: 2px solid var(--rule); }
</style>
</head>
<body>

<section class="card card--front">
  <div class="pool-photo" role="img" aria-label="Photo of an elegant modern home beside a lit swimming pool, with a light grey silhouette of a woman holding a cleaning pole on the left"></div>
  <svg class="layer" width="672" height="520" viewBox="0 0 672 520" aria-hidden="true">
    <defs>
      <linearGradient id="topBand" x1="0" y1="0" x2="1" y2="0">
        <stop offset="0" stop-color="#f2f9fc"/><stop offset="1" stop-color="#bfe3f2"/>
      </linearGradient>
    </defs>
    <path d="M0 0 H672 V55 C560 60 420 125 200 125 C110 125 40 112 0 95 Z" fill="url(#topBand)"/>
    <path d="M0 88 C60 118 150 130 240 124 C330 118 370 100 380 95" fill="none" stroke="#5cc6ef" stroke-width="5"/>
    <path d="M0 412 C180 380 420 395 672 430 V520 H0 Z" fill="#2a86c3"/>
    <path d="M0 424 C200 398 430 418 672 446 V520 H0 Z" fill="#0e5b8f"/>
  </svg>

  <div class="abs company" style="left:30px; top:16px; font-size:24px; letter-spacing:4px;">KRT Pool &amp; Spa Cleaning</div>
  <div class="abs nickname" style="left:100px; top:52px; font-size:34px;">The Tide Lady</div>

  <div class="abs brand" style="left:436px; top:90px; font-size:42px; gap:10px;"><span class="brand-square" style="width:22px; height:22px;"></span>KRT Pools</div>
  <div class="abs license" style="left:570px; top:175px; font-size:12px; color:var(--white);">Lic.# 318604</div>

  <div class="abs offer-big" style="left:180px; top:158px; font-size:76px;">50% <span style="font-size:44px;">off</span></div>
  <div class="abs offer-line" style="left:184px; top:246px;">First Month of Maintenance,</div>
  <div class="abs offer-line" style="left:200px; top:274px;">Very Reasonable&nbsp; Rates !!</div>
  <div class="abs insured" style="left:352px; top:304px;">(Insured)</div>

  <svg class="abs" style="left:26px; top:438px;" width="22" height="22" viewBox="0 0 22 22" aria-hidden="true">
    <circle cx="11" cy="11" r="11" fill="#ffffff"/>
    <path d="M8 6 L14 11 L8 16" fill="none" stroke="#0e5b8f" stroke-width="3"/>
  </svg>
  <div class="abs service" style="left:58px; top:440px;">We provide&nbsp; weekly cleaning maintenance service on in ground swimming pool's &amp; spa's</div>

  <div class="abs prompt" style="left:455px; top:436px; font-size:13px; color:#8fd3f4;">Call us now for a free estimate!</div>
  <svg class="abs" style="left:402px; top:448px;" width="40" height="36" viewBox="0 0 40 36" aria-hidden="true">
    <path d="M4 12 C4 4 36 4 36 12 L36 16 L28 16 L28 12 L12 12 L12 16 L4 16 Z" fill="#ffffff"/>
    <path d="M10 18 L30 18 L36 34 L4 34 Z" fill="#ffffff"/>
    <circle cx="20" cy="26" r="5" fill="#0e5b8f"/>
  </svg>
  <div class="abs phone" style="left:460px; top:452px; font-size:27px; color:var(--white);">951-478-2051</div>
  <div class="abs" style="left:460px; top:485px; font-size:14px; font-weight:600; color:#bfe6fb;">k_kwaterfresh@mailvale.com</div>
</section>

<section class="card card--back">
  <svg class="layer" width="672" height="520" viewBox="0 0 672 520" aria-hidden="true">
    <path d="M0 110 C80 140 200 150 355 138 C300 150 160 158 0 128 Z" fill="#5cc6ef"/>
    <path d="M0 470 C200 430 450 455 672 452 V520 H0 Z" fill="#2a86c3"/>
    <path d="M0 478 C220 448 460 470 672 466 V520 H0 Z" fill="#0e5b8f"/>
  </svg>

  <div class="abs brand" style="left:44px; top:42px; font-size:22px; gap:6px;"><span class="brand-square" style="width:18px; height:18px;"></span>KRT Pools</div>
  <div class="abs nickname" style="left:170px; top:38px; font-size:34px;">The Tide Lady</div>
  <div class="abs company" style="left:60px; top:98px; font-size:22px; letter-spacing:1px;">KRT Pool &amp; Spa Cleaning</div>
  <div class="abs license" style="left:142px; top:138px; font-size:15px; color:var(--navy);">Lic.# 318604</div>

  <div class="abs prompt" style="left:50px; top:180px; font-size:17px; color:var(--sky);">Call us now for a free estimate!</div>
  <svg class="abs" style="left:50px; top:206px;" width="40" height="36" viewBox="0 0 40 36" aria-hidden="true">
    <path d="M4 12 C4 4 36 4 36 12 L36 16 L28 16 L28 12 L12 12 L12 16 L4 16 Z" fill="#2a90cf"/>
    <path d="M10 18 L30 18 L36 34 L4 34 Z" fill="#2a90cf"/>
    <circle cx="20" cy="26" r="5" fill="#ffffff"/>
  </svg>
  <div class="abs phone" style="left:107px; top:208px; font-size:27px; color:var(--sky);">951-478-2051</div>
  <div class="abs" style="left:110px; top:242px; font-size:16px; font-weight:600; color:var(--sky);">k_kwaterfresh@mailvale.com</div>

  <div class="stamp-box"></div>
  <div class="address-line" style="top:176px;"></div>
  <div class="address-line" style="top:204px;"></div>
  <div class="address-line" style="top:232px;"></div>
  <div class="address-line" style="top:260px;"></div>
  <div class="address-line" style="top:288px;"></div>

  <div class="splash" role="img" aria-label="Decorative blue water splash with droplets"></div>
  <div class="portrait" role="img" aria-label="Portrait photo of the owner outdoors on a lawn"></div>
</section>

</body>
</html>
```